Brennick Capital Business Cards

These are professional business cards that are for my family office.
Put fake emails and phone numbers as of now until I finalize those components. This family office controls my families investments, assets, and future. The cards should be professional.
..
.
.
.
I just uploaded another variation of a logo I would like to see as a business card to I am inbeteen which logo to use

Target Market(s)

business

Industry/Entity Type

business

Contact Information for Business Card

Professional, wealth related, finance related.

Requirements
Must have
• Logo

```html
<!DOCTYPE html>
<html lang="en">
<head>
<meta charset="utf-8">
<title>Brennick Capital – Business Card</title>
<link rel="stylesheet" href="https://fonts.googleapis.com/css2?family=Playfair+Display:wght@400;500&family=Poppins:wght@400&display=swap">
<style>
  :root {
    --backdrop: #2b2b2d;
    --card-white: #ffffff;
    --card-black: #141416;
    --ink: #111111;
    --gold: #c3a96b;
    --rule: #9a9a9a;
    --pattern-light: #2a2a2d;
    --pattern-dark: #0c0c0e;
  }
  * { box-sizing: border-box; margin: 0; padding: 0; }
  html, body {
    width: 1200px;
    height: 1108px;
    overflow: hidden;
    background: var(--backdrop);
  }
  .stage {
    position: relative;
    width: 1200px;
    height: 1108px;
  }
  .card {
    position: absolute;
    top: 199px;
    width: 400px;
    height: 700px;
    border-radius: 22px;
    overflow: hidden;
  }
  .card-front {
    left: 160px;
    background: var(--card-white);
    text-align: center;
    color: var(--ink);
  }
  .card-back {
    left: 640px;
    background: var(--card-black);
  }

  /* Front */
  .brand-name {
    margin-top: 150px;
    font-family: "Playfair Display", serif;
    font-weight: 400;
    font-size: 38px;
    line-height: 1.15;
    letter-spacing: 1px;
    text-transform: uppercase;
    color: var(--ink);
  }
  .person-name {
    margin-top: 150px;
    font-family: "Playfair Display", serif;
    font-weight: 400;
    font-size: 30px;
    letter-spacing: 0.5px;
    text-transform: uppercase;
    white-space: nowrap;
  }
  .person-name .surname { color: var(--gold); }
  .person-title {
    margin-top: 2px;
    font-family: "Poppins", sans-serif;
    font-size: 17px;
    color: var(--gold);
  }
  .icon-row {
    display: flex;
    align-items: center;
    justify-content: center;
    gap: 6px;
    margin: 14px 40px 8px;
  }
  .icon-row .rule {
    flex: 1;
    height: 1px;
    background: var(--rule);
  }
  .icon-badge {
    width: 28px;
    height: 28px;
    border-radius: 5px;
    background: var(--gold);
    display: flex;
    align-items: center;
    justify-content: center;
  }
  .contact-list {
    font-family: "Poppins", sans-serif;
    font-size: 17px;
    line-height: 1.45;
  }
  .divider {
    height: 1px;
    background: var(--rule);
    margin: 16px 60px 14px;
  }
  .address {
    font-family: "Poppins", sans-serif;
    font-size: 16px;
    line-height: 1.4;
  }

  /* Back */
  .back-pattern {
    position: absolute;
    inset: 0;
    background: linear-gradient(135deg, var(--pattern-light) 0%, var(--card-black) 45%, var(--pattern-dark) 100%);
  }
  .back-mark {
    position: absolute;
    right: 36px;
    bottom: 44px;
    display: flex;
    align-items: center;
    gap: 8px;
    font-family: "Playfair Display", serif;
    font-size: 15px;
    letter-spacing: 1px;
    text-transform: uppercase;
    color: var(--card-white);
  }
  .back-mark .dot {
    width: 10px;
    height: 10px;
    background: var(--card-white);
  }
</style>
</head>
<body>
<main class="stage">

  <section class="card card-front" aria-label="Business card front">
    <h1 class="brand-name">Brennick<br>Capital</h1>

    <p class="person-name">Adrian <span class="surname">Holloway</span></p>
    <p class="person-title">Managing Director</p>

    <div class="icon-row">
      <span class="rule"></span>
      <span class="icon-badge" aria-label="Phone">
        <svg width="16" height="16" viewBox="0 0 24 24" fill="#fff"><path d="M6.6 10.8a15 15 0 0 0 6.6 6.6l2.2-2.2a1 1 0 0 1 1-.25 11.4 11.4 0 0 0 3.6.57 1 1 0 0 1 1 1V20a1 1 0 0 1-1 1A17 17 0 0 1 3 4a1 1 0 0 1 1-1h3.5a1 1 0 0 1 1 1c0 1.25.2 2.45.57 3.57a1 1 0 0 1-.25 1z"/></svg>
      </span>
      <span class="icon-badge" aria-label="Email">
        <svg width="16" height="16" viewBox="0 0 24 24" fill="none" stroke="#fff" stroke-width="2"><rect x="3" y="5" width="18" height="14" rx="1"/><path d="M3 6l9 7 9-7"/></svg>
      </span>
      <span class="icon-badge" aria-label="Website">
        <svg width="16" height="16" viewBox="0 0 24 24" fill="none" stroke="#fff" stroke-width="2"><circle cx="12" cy="12" r="9"/><path d="M3 12h18M12 3c3 3 3 15 0 18M12 3c-3 3-3 15 0 18"/></svg>
      </span>
      <span class="rule"></span>
    </div>

    <div class="contact-list">
      <p>055-318 274 960</p>
      <p>office@brennickcap.com</p>
      <p>www.brennickcap.com</p>
    </div>

    <div class="divider"></div>

    <p class="address">88 Harbor Row, Suite 300<br>60614, Northvale</p>
  </section>

  <section class="card card-back" aria-label="Business card back">
    <div class="back-pattern" role="img" aria-label="Repeating glossy brand pattern on black"></div>
    <div class="back-mark"><span class="dot"></span>Brennick Capital</div>
  </section>

</main>
</body>
</html>
```